Venlow Partners
Global Real Estate Investing
Venlow Partners -
Creative Brief
Modern
Ravi Talbert
President
24817 Mobley Lane 2nd Floor Southgate MI 48195
rtalbert@venlowpartners.example
www.venlowpartners.example

```html
<!DOCTYPE html>
<html lang="en">
<head>
<meta charset="UTF-8">
<title>Venlow Partners – Business Card</title>
<link href="https://fonts.googleapis.com/css2?family=Arimo:wght@400;700&family=PT+Sans:wght@400;700&display=swap" rel="stylesheet">
<style>
  :root {
    --backdrop: #2b2b2d;
    --card: #ffffff;
    --navy: #152a6e;
    --band-top: #1b2f72;
    --band-bottom: #3a6de0;
    --text-grey: #55575c;
    --faint: #e8edf6;
  }
  html, body {
    margin: 0;
    padding: 0;
    width: 1200px;
    height: 780px;
    overflow: hidden;
    background: var(--backdrop);
  }
  .business-card {
    position: absolute;
    left: 80px;
    top: 90px;
    width: 1040px;
    height: 600px;
    background: var(--card);
    border-radius: 34px;
    overflow: hidden;
    font-family: "Arimo", Arial, sans-serif;
  }
  .side-band {
    position: absolute;
    left: 0;
    top: 0;
    width: 74px;
    height: 100%;
    background: linear-gradient(180deg, var(--band-top) 0%, var(--band-bottom) 100%);
  }
  .band-icons {
    position: absolute;
    left: 0;
    top: 0;
    width: 74px;
    height: 600px;
  }
  .brand {
    position: absolute;
    left: 40px;
    top: 70px;
    display: flex;
    align-items: center;
    gap: 26px;
  }
  .brand-mark {
    width: 96px;
    height: 96px;
    border-radius: 50%;
    background: var(--card);
    border: 8px solid var(--navy);
    box-sizing: border-box;
  }
  .brand-name {
    font-weight: 700;
    font-size: 46px;
    line-height: 1;
    color: var(--navy);
    letter-spacing: 1px;
    white-space: nowrap;
  }
  .faint-circle {
    position: absolute;
    left: 580px;
    top: 220px;
    width: 200px;
    height: 200px;
    border-radius: 50%;
    border: 14px solid var(--faint);
    box-sizing: border-box;
  }
  .address {
    position: absolute;
    left: 160px;
    top: 288px;
    margin: 0;
    font-size: 21px;
    line-height: 30px;
    color: var(--text-grey);
    font-style: normal;
  }
  .contact-list {
    position: absolute;
    left: 160px;
    top: 384px;
    margin: 0;
    padding: 0;
    list-style: none;
    font-size: 21px;
    line-height: 32px;
    color: var(--text-grey);
  }
  .holder {
    position: absolute;
    right: 60px;
    top: 286px;
    width: 260px;
    text-align: right;
    font-family: "PT Sans", Arial, sans-serif;
  }
  .holder-name {
    margin: 0;
    font-size: 36px;
    line-height: 42px;
    font-weight: 700;
    color: var(--navy);
  }
  .holder-title {
    margin: 2px 0 0;
    font-size: 24px;
    line-height: 30px;
    color: var(--navy);
    padding-right: 40px;
  }
</style>
</head>
<body>
  <article class="business-card">
    <div class="side-band"></div>

    <svg class="band-icons" viewBox="0 0 74 600" aria-hidden="true" fill="#ffffff">
      <path class="icon-home" d="M37 292 l-13 11 h4 v11 h7 v-7 h4 v7 h7 v-11 h4 z"/>
      <path class="icon-phone" d="M29 392 c2 -2 5 -2 6 0 l2 4 c1 2 0 3 -1 4 l-1 1 c1 3 3 5 6 6 l1 -1 c1 -1 3 -2 4 -1 l4 2 c2 1 2 4 0 6 l-2 2 c-8 2 -21 -11 -19 -19 z"/>
      <rect class="icon-fax" x="27" y="428" width="20" height="12" rx="2"/>
      <rect x="31" y="422" width="12" height="5"/>
      <text class="icon-email" x="37" y="471" font-family="Arimo, Arial, sans-serif" font-size="20" font-weight="700" text-anchor="middle">@</text>
      <g class="icon-web" fill="none" stroke="#ffffff" stroke-width="2">
        <circle cx="37" cy="496" r="9"/>
        <line x1="28" y1="496" x2="46" y2="496"/>
        <ellipse cx="37" cy="496" rx="4" ry="9"/>
      </g>
    </svg>

    <div class="brand">
      <div class="brand-mark"></div>
      <div class="brand-name">Venlow Partners</div>
    </div>

    <div class="faint-circle"></div>

    <address class="address">
      24817 Mobley Lane 2nd Floor<br>
      Larkfield MI 48920
    </address>

    <ul class="contact-list">
      <li>734-555-0147</li>
      <li>734-555-0182</li>
      <li>rtalbert@venlowpartners.example</li>
      <li>www.venlowpartners.example</li>
    </ul>

    <div class="holder">
      <p class="holder-name">Ravi Talbert</p>
      <p class="holder-title">President</p>
    </div>
  </article>
</body>
</html>
```